Higher co-efficient of performance means more heat for your money

I need a bar graph that will have the following heating systems, 80% efficient gas furnace COP of .8, Electric heat COP of 1, and Our best selling heat pump with a cop of 4 at 47F. I will have a constant bar, 100$ worth of gas for furnace, 100$ of electricity for electric heat, and 100$ worth of electricity for our heat pumps. next to them I will have a bar showing how much heat each heating system will provide for $100 of fuel. For gas furnace I need a bar that says $80 worth of heat and the barograph to match it, for electric heat I need the bar to show 100$ worth of heat, for our best selling heat pump I need the bar graph to show and say $400 dollars worth of heat. Please take a look at my website www.summitbreezecomfort.example for brand color and feel

```html
<!DOCTYPE html>
<html lang="en">
<head>
<meta charset="utf-8">
<title>Higher Co-Efficient of Performance – Summit Breeze Comfort</title>
<link rel="stylesheet" href="https://fonts.googleapis.com/css2?family=Audiowide&family=Roboto:wght@400;700&display=swap">
<style>
  :root {
    --paper: #f6f7f9;
    --brand-red: #c9262f;
    --brand-red-dark: #8c161d;
    --brand-blue: #1f77bb;
    --brand-blue-dark: #135282;
    --ink: #2b2b2b;
    --axis: #4a4a4a;
    --tick-warm: #f0b9a8;
    --tick-cool: #b9cbe6;
  }
  html, body {
    margin: 0;
    padding: 0;
    width: 1200px;
    height: 1200px;
    overflow: hidden;
    background: var(--paper);
  }
  .poster {
    position: relative;
    width: 1200px;
    height: 1200px;
    background: var(--paper);
    font-family: "Roboto", Arial, sans-serif;
  }
  .headline {
    position: absolute;
    left: 108px;
    top: 100px;
    margin: 0;
    font-family: "Audiowide", sans-serif;
    font-weight: 400;
    font-size: 38px;
    line-height: 46px;
    letter-spacing: 0.5px;
    color: var(--brand-blue);
  }
  .headline .accent { color: var(--brand-red); }
  .divider {
    position: absolute;
    left: 108px;
    top: 286px;
    width: 45px;
    height: 2px;
    background: var(--ink);
  }
  .footnote {
    position: absolute;
    left: 108px;
    top: 314px;
    margin: 0;
    font-family: "Roboto", Arial, sans-serif;
    font-weight: 700;
    font-size: 22px;
    color: var(--brand-red);
  }
  .brand {
    position: absolute;
    left: 860px;
    top: 150px;
    width: 250px;
    display: flex;
    flex-direction: column;
    align-items: center;
    gap: 14px;
  }
  .brand-dot {
    width: 64px;
    height: 64px;
    border-radius: 50%;
    background: var(--brand-blue);
  }
  .brand-name {
    font-family: "Audiowide", sans-serif;
    font-size: 24px;
    line-height: 28px;
    text-align: center;
    color: var(--brand-blue);
  }
  .chart {
    position: absolute;
    left: 0;
    top: 0;
    width: 1200px;
    height: 1200px;
  }
  .axis-label { font-family: "Roboto", Arial, sans-serif; font-size: 20px; fill: var(--ink); }
  .temp-label { font-family: "Roboto", Arial, sans-serif; font-size: 15px; fill: var(--ink); }
  .legend-label { font-family: "Audiowide", sans-serif; font-size: 20px; fill: var(--ink); }
  .category-label { font-family: "Audiowide", sans-serif; font-size: 18px; fill: var(--ink); }
</style>
</head>
<body>
<main class="poster">
  <h1 class="headline">
    <span class="accent">HIGHER CO-EFFICIENT OF<br>PERFORMANCE</span> MEANS MORE<br>HEAT FOR YOUR MONEY
  </h1>
  <div class="divider"></div>
  <p class="footnote">*COP Measure At 47° F</p>

  <div class="brand">
    <div class="brand-dot"></div>
    <div class="brand-name">SUMMIT BREEZE<br>COMFORT</div>
  </div>

  <svg class="chart" viewBox="0 0 1200 1200" xmlns="http://www.w3.org/2000/svg">
    <defs>
      <linearGradient id="cost-fill" x1="0" y1="0" x2="0" y2="1">
        <stop offset="0" stop-color="var(--brand-red-dark)"/>
        <stop offset="1" stop-color="var(--brand-red)"/>
      </linearGradient>
      <linearGradient id="heat-fill" x1="0" y1="0" x2="0" y2="1">
        <stop offset="0" stop-color="var(--brand-blue-dark)"/>
        <stop offset="1" stop-color="var(--brand-blue)"/>
      </linearGradient>
      <g id="thermometer" fill="none" stroke="var(--brand-blue)" stroke-width="2">
        <path d="M-3 -14 a3 3 0 0 1 6 0 v16 a6 6 0 1 1 -6 0 z"/>
        <circle cx="0" cy="7" r="2.5" fill="var(--brand-blue)" stroke="none"/>
        <line x1="0" y1="-8" x2="0" y2="5"/>
      </g>
    </defs>

    <!-- dollar scale -->
    <g class="dollar-scale" text-anchor="end">
      <text class="axis-label" x="161" y="500">$400</text>
      <text class="axis-label" x="161" y="561">$350</text>
      <text class="axis-label" x="161" y="626">$300</text>
      <text class="axis-label" x="161" y="694">$250</text>
      <text class="axis-label" x="161" y="761">$200</text>
      <text class="axis-label" x="161" y="826">$150</text>
      <text class="axis-label" x="161" y="892">$100</text>
      <text class="axis-label" x="161" y="957">$50</text>
      <text class="axis-label" x="161" y="1022">$0</text>
    </g>

    <!-- temperature scale -->
    <g class="temp-scale">
      <line x1="1059" y1="501" x2="1059" y2="1020" stroke="var(--tick-cool)" stroke-width="2"/>
      <g stroke-width="2">
        <line x1="1048" y1="532" x2="1058" y2="532" stroke="var(--tick-warm)"/>
        <line x1="1045" y1="564" x2="1058" y2="564" stroke="var(--tick-cool)"/>
        <line x1="1048" y1="597" x2="1058" y2="597" stroke="var(--tick-warm)"/>
        <line x1="1045" y1="629" x2="1058" y2="629" stroke="var(--tick-cool)"/>
        <line x1="1048" y1="662" x2="1058" y2="662" stroke="var(--tick-warm)"/>
        <line x1="1045" y1="694" x2="1058" y2="694" stroke="var(--tick-cool)"/>
        <line x1="1048" y1="726" x2="1058" y2="726" stroke="var(--tick-warm)"/>
        <line x1="1045" y1="759" x2="1058" y2="759" stroke="var(--tick-cool)"/>
        <line x1="1048" y1="791" x2="1058" y2="791" stroke="var(--tick-warm)"/>
        <line x1="1045" y1="824" x2="1058" y2="824" stroke="var(--tick-cool)"/>
        <line x1="1048" y1="856" x2="1058" y2="856" stroke="var(--tick-warm)"/>
        <line x1="1045" y1="889" x2="1058" y2="889" stroke="var(--tick-cool)"/>
        <line x1="1048" y1="923" x2="1058" y2="923" stroke="var(--tick-warm)"/>
        <line x1="1045" y1="955" x2="1058" y2="955" stroke="var(--tick-cool)"/>
        <line x1="1048" y1="987" x2="1058" y2="987" stroke="var(--tick-warm)"/>
      </g>
      <text class="temp-label" x="1072" y="537">75° F</text>
      <text class="temp-label" x="1072" y="569">70° F</text>
      <text class="temp-label" x="1072" y="602">65° F</text>
      <text class="temp-label" x="1072" y="634">60° F</text>
      <text class="temp-label" x="1072" y="667">55° F</text>
      <text class="temp-label" x="1072" y="699">50° F</text>
      <text class="temp-label" x="1072" y="731">45° F</text>
      <text class="temp-label" x="1072" y="764">40° F</text>
      <text class="temp-label" x="1072" y="796">35° F</text>
      <text class="temp-label" x="1072" y="829">30° F</text>
      <text class="temp-label" x="1072" y="861">25° F</text>
      <text class="temp-label" x="1072" y="894">20° F</text>
      <text class="temp-label" x="1072" y="928">15° F</text>
      <text class="temp-label" x="1072" y="960">10° F</text>
      <text class="temp-label" x="1072" y="992">5° F</text>
      <text class="temp-label" x="1072" y="1023">0° F</text>
    </g>

    <!-- legend -->
    <g class="legend">
      <rect x="223" y="585" width="29" height="29" fill="var(--brand-red)"/>
      <text class="legend-label" x="268" y="607">ELECTRICITY COST</text>
      <rect x="223" y="634" width="29" height="29" fill="var(--brand-blue)"/>
      <text class="legend-label" x="268" y="656">HEAT GENERATED</text>
    </g>

    <!-- bars -->
    <g class="bars">
      <rect x="224" y="889" width="72" height="131" fill="url(#cost-fill)"/>
      <rect x="319" y="915" width="72" height="105" fill="url(#heat-fill)"/>
      <rect x="495" y="889" width="72" height="131" fill="url(#cost-fill)"/>
      <rect x="590" y="889" width="72" height="131" fill="url(#heat-fill)"/>
      <rect x="826" y="889" width="72" height="131" fill="url(#cost-fill)"/>
      <rect x="920" y="495" width="72" height="525" fill="url(#heat-fill)"/>
    </g>

    <!-- bar icons -->
    <g class="bar-icons">
      <path d="M260 838 C252 850 247 858 247 866 a13 13 0 0 0 26 0 c0 -8 -5 -16 -13 -28 z" fill="var(--brand-red)"/>
      <path d="M533 838 l-12 22 h8 l-5 17 l14 -23 h-8 l7 -16 z" fill="var(--brand-red)"/>
      <use href="#thermometer" x="355" y="880"/>
      <use href="#thermometer" x="626" y="855"/>
      <use href="#thermometer" x="956" y="462"/>
      <g fill="none" stroke="var(--brand-red)" stroke-width="2">
        <line x1="836" y1="868" x2="883" y2="868"/>
        <rect x="845" y="864" width="29" height="8" fill="var(--paper)"/>
        <line x1="852" y1="866" x2="852" y2="870"/>
        <line x1="859" y1="866" x2="859" y2="870"/>
        <line x1="866" y1="866" x2="866" y2="870"/>
      </g>
    </g>

    <!-- baseline -->
    <line x1="174" y1="1020" x2="1059" y2="1020" stroke="var(--axis)" stroke-width="2"/>

    <!-- categories -->
    <g class="categories" text-anchor="middle">
      <text class="category-label" x="311" y="1061">Gas</text>
      <text class="category-label" x="311" y="1084">Function</text>
      <text class="category-label" x="585" y="1061">Electric</text>
      <text class="category-label" x="585" y="1084">Heat</text>
      <text class="category-label" x="917" y="1061">Our Best Selling</text>
      <text class="category-label" x="917" y="1084">Heat Pump</text>
    </g>
  </svg>
</main>
</body>
</html>
```